Business Card Design Z9 MOTORS

Hi firstly I would like you to design a professional logo for my company. By using words " Z9 Auto Spares & Haulage".
We are an auto dismantling company where we buy wrecks/cars for dismantling and selling salvageable parts again.

Hi every one,

Thank you for posting the designs. But unfortunately non of these designs have the logo that I would prefer for my company. I will be branding the logo quite extensively, therefore please design some professional looking ones.

Thanks

Industry/Entity Type

Business

Contact Information for Business Card

Z9 Auto Spares & Haulage, 472 Kowhai Bend Rd, Fernmoor, Wellington
T: 04 7261048, F: 04 7261049, E: dean.morrow@z9motors.example.nz, W: www.z9motors.example.nz
Name: Dean L Morrow
Managing Director
Mob: 027418906

At the bottom of card " WE PAY TOP $$$$ FOR ANY UNWANTED VEHICLES FOR FOR DISMANTLING CALL US NOW 0800372815"

```html
<!DOCTYPE html>
<html lang="en">
<head>
<meta charset="utf-8">
<title>Z9 Auto Spares &amp; Haulage – Business Card</title>
<link rel="stylesheet" href="https://fonts.googleapis.com/css2?family=Montserrat:wght@300;400;500;600&family=Oswald:wght@600&display=swap">
<style>
  :root {
    --canvas: #e7e5e2;
    --card-black: #0b0b0c;
    --card-graphite: #262628;
    --brand-red: #b51a2a;
    --brand-red-dark: #7d0f1b;
    --silver: #c9c9cc;
    --white: #ffffff;
    --name-red: #c8202f;
  }
  * { box-sizing: border-box; margin: 0; padding: 0; }
  html, body { width: 1200px; height: 1000px; overflow: hidden; }
  body {
    background: var(--canvas);
    font-family: "Montserrat", Arial, sans-serif;
    color: var(--white);
    position: relative;
  }
  .card {
    position: absolute;
    left: 250px;
    width: 700px;
    height: 400px;
    border-radius: 28px;
    overflow: hidden;
    background: var(--card-black);
    box-shadow: 0 8px 24px rgba(0,0,0,.25);
  }
  .card--front { top: 70px; }
  .card--back { top: 530px; }

  .machinery-art {
    position: absolute;
    inset: 0;
    background:
      radial-gradient(circle at 62% 38%, var(--card-graphite) 0%, #161617 40%, var(--card-black) 75%);
  }

  /* front */
  .front-brand {
    position: absolute;
    left: 120px;
    top: 150px;
    display: flex;
    align-items: center;
    gap: 16px;
    white-space: nowrap;
  }
  .front-brand__mark {
    width: 30px; height: 30px;
    background: var(--brand-red);
  }
  .front-brand__name {
    font-size: 32px;
    font-weight: 600;
    color: var(--white);
    letter-spacing: .5px;
  }
  .slogan-band {
    position: absolute;
    left: 0; right: 0; bottom: 0;
    height: 92px;
    background: linear-gradient(180deg, var(--brand-red) 0%, var(--brand-red-dark) 100%);
    border-top: 5px solid var(--silver);
    display: flex;
    flex-direction: column;
    align-items: center;
    justify-content: center;
    text-align: center;
    font-size: 15px;
    font-weight: 400;
    line-height: 1.35;
    letter-spacing: .6px;
    text-transform: uppercase;
  }

  /* back */
  .back-title {
    position: absolute;
    left: 48px;
    top: 28px;
    font-family: "Oswald", "Arial Narrow", sans-serif;
    font-weight: 600;
    font-size: 40px;
    color: var(--white);
    white-space: nowrap;
  }
  .back-brand {
    position: absolute;
    right: 36px;
    top: 96px;
    font-size: 26px;
    font-weight: 600;
    color: var(--name-red);
    white-space: nowrap;
  }
  .person {
    position: absolute;
    left: 40px;
    top: 98px;
    white-space: nowrap;
  }
  .person__name {
    font-size: 28px;
    font-weight: 600;
    color: var(--name-red);
  }
  .person__role {
    font-size: 24px;
    font-weight: 300;
    color: var(--white);
    margin-top: 2px;
  }
  .contact-panel {
    position: absolute;
    left: 0; right: 0; bottom: 0;
    height: 225px;
    background: linear-gradient(180deg, var(--brand-red) 0%, var(--brand-red-dark) 100%);
    border-top: 5px solid var(--silver);
  }
  .contact-list {
    list-style: none;
    position: absolute;
    left: 40px;
    top: 24px;
    font-size: 18px;
    font-weight: 400;
    line-height: 32px;
    white-space: nowrap;
  }
  .contact-list li { display: flex; align-items: center; gap: 10px; }
  .contact-list svg { width: 17px; height: 17px; flex: none; }
  .address {
    position: absolute;
    right: 36px;
    bottom: 26px;
    text-align: right;
    font-size: 19px;
    font-weight: 400;
    line-height: 28px;
    font-style: normal;
    white-space: nowrap;
  }
  .address__label { font-weight: 600; }
</style>
</head>
<body>

<section class="card card--front">
  <div class="machinery-art" role="img" aria-label="Dark embossed illustration of wheels, gears and engine parts"></div>
  <div class="front-brand">
    <span class="front-brand__mark"></span>
    <span class="front-brand__name">Z9 Auto Spares &amp; Haulage</span>
  </div>
  <div class="slogan-band">
    <p>" We pay top $$$$ for any unwanted vehicles for for dismantling</p>
    <p>call us now 0800372815"</p>
  </div>
</section>

<section class="card card--back">
  <div class="machinery-art" role="img" aria-label="Dark embossed illustration of wheels, gears and engine parts"></div>
  <h1 class="back-title">Z9 Auto Spares &amp; Haulage</h1>
  <div class="back-brand">Z9 MOTORS</div>
  <div class="person">
    <p class="person__name">Dean L Morrow</p>
    <p class="person__role">Managing Director</p>
  </div>
  <div class="contact-panel">
    <ul class="contact-list">
      <li>
        <svg viewBox="0 0 24 24" fill="#fff"><path d="M6.6 10.8a15 15 0 0 0 6.6 6.6l2.2-2.2a1 1 0 0 1 1-.25 11 11 0 0 0 3.6.6 1 1 0 0 1 1 1V20a1 1 0 0 1-1 1A17 17 0 0 1 3 4a1 1 0 0 1 1-1h3.5a1 1 0 0 1 1 1 11 11 0 0 0 .6 3.6 1 1 0 0 1-.25 1z"/></svg>
        04 7261048
      </li>
      <li>
        <svg viewBox="0 0 24 24" fill="#fff"><path d="M7 3h10v5H7zM4 9h16a2 2 0 0 1 2 2v6h-4v4H6v-4H2v-6a2 2 0 0 1 2-2zm4 7v3h8v-3z"/></svg>
        04 7261049
      </li>
      <li>
        <svg viewBox="0 0 24 24" fill="none" stroke="#fff" stroke-width="2"><rect x="7" y="2" width="10" height="20" rx="2"/><line x1="11" y1="18" x2="13" y2="18"/></svg>
        027418906
      </li>
      <li>
        <svg viewBox="0 0 24 24" fill="none" stroke="#fff" stroke-width="2"><rect x="2" y="5" width="20" height="14"/><polyline points="2,5 12,13 22,5"/></svg>
        dean.morrow@z9motors.example.nz
      </li>
      <li>
        <svg viewBox="0 0 24 24" fill="none" stroke="#fff" stroke-width="2"><circle cx="12" cy="12" r="10"/><ellipse cx="12" cy="12" rx="4" ry="10"/><line x1="2" y1="12" x2="22" y2="12"/></svg>
        www.z9motors.example.nz
      </li>
    </ul>
    <address class="address">
      <p class="address__label">Address</p>
      <p>472 Kowhai Bend Rd,</p>
      <p>Fernmoor,</p>
      <p>Wellington</p>
    </address>
  </div>
</section>

</body>
</html>
```